Monthly Mailed Newsletter/Magazine for Medical Spa

Every month we send out a mailed newsletter/magazine to our visitors from the previous month. We made a sample newsletter/magazine as a guideline of what we are looking for. We need a designer to make a simple and clean design layout.

- Attached is our sample design that has all the content we want to use.
- Newsletter/magazine is 8 pages total.
- Size of each page is 8.5 inches in width by 11 inches in height.
- Content and images can be located here: https://files.quorvadrop.net/share/folders/8kTrmWq2Zp7ncV4Lx91aHd0sYuE3Gb6Rj?access=open

The following will give you an idea of our brand presentation.
Our website is: www.FernBloomClinic.com
Our Instagram; @fernbloomclinic
Our Facebook: www.friendvault.com/fernbloomclinic

Target Market(s)

Women 25 - 45

Industry/Entity Type

Beauty

Other font styles liked:
• Josefins Sans Bold & Lato

Colors
f78f20
ffffff

Requirements
Must have
• - Our Logo
- Our tagline: YOUR SKIN DESERVES IT!
- Address and contact information for our locations
- Our color scheme: Black and #FAA641
- Heading font is Josefin Sans Bold
- Paragraph font is Lato
- Our website address: www.FernBloomClinic.com

```html
<!DOCTYPE html>
<html lang="en">
<head>
<meta charset="UTF-8">
<title>Fern Bloom Clinic — Newsletter Cover</title>
<link href="https://fonts.googleapis.com/css2?family=Josefin+Sans:wght@700&family=Lato:wght@400;700&display=swap" rel="stylesheet">
<style>
  :root {
    --backdrop: #fbb866;
    --paper: #ffffff;
    --brand-orange: #f6a23a;
    --tint: rgba(247, 150, 40, 0.42);
    --charcoal-bar: rgba(70, 66, 64, 0.85);
    --ink: #2a2a2a;
    --black: #111111;
  }
  * { margin: 0; padding: 0; box-sizing: border-box; }
  html, body {
    width: 1200px; height: 1200px; overflow: hidden;
    background: var(--backdrop);
  }
  .cover {
    position: absolute; left: 175px; top: 50px;
    width: 850px; height: 1100px;
    background: var(--paper);
    overflow: hidden;
  }
  .brand-name {
    position: absolute; right: 73px; top: 150px;
    font-family: "Lato", sans-serif; font-weight: 700;
    font-size: 32px; line-height: 1;
    color: var(--black);
    white-space: nowrap;
  }
  .accent-bar {
    position: absolute; left: 0; top: 216px;
    width: 201px; height: 63px;
    background: var(--charcoal-bar);
    z-index: 1;
  }
  .hero-photo {
    position: absolute; left: 202px; top: 371px;
    width: 649px; height: 610px;
    background: linear-gradient(120deg, #c9b49c 0%, #b9aa9a 40%, #a9b3b3 65%, #8b6f5a 100%);
  }
  .tint-panel {
    position: absolute; left: 50px; top: 251px;
    width: 429px; height: 776px;
    background: var(--tint);
    z-index: 2;
  }
  .headline-top {
    position: absolute; left: 322px; top: 280px;
    font-family: "Josefin Sans", sans-serif; font-weight: 700;
    font-size: 82px; line-height: 1;
    color: var(--brand-orange);
    white-space: nowrap; z-index: 3;
  }
  .headline-side {
    position: absolute; left: 104px; top: 395px;
    writing-mode: vertical-rl;
    font-family: "Josefin Sans", sans-serif; font-weight: 700;
    font-size: 84px; line-height: 1;
    color: var(--ink);
    white-space: nowrap; z-index: 3;
  }
  .issue-line {
    position: absolute; right: 50px; top: 1049px;
    font-family: "Lato", sans-serif; font-size: 16px;
    color: var(--black);
  }
</style>
</head>
<body>
  <main class="cover">
    <p class="brand-name">Fern Bloom Clinic</p>

    <div class="accent-bar"></div>
    <div class="hero-photo" role="img" aria-label="Photo of a technician in scrubs giving a laser treatment to a smiling client lying on a treatment bed, both wearing protective glasses"></div>
    <div class="tint-panel"></div>

    <h1 class="headline-top">YOUR SKIN</h1>
    <p class="headline-side">DESERVES IT!</p>

    <p class="issue-line">NOV2020 | VOL 1</p>
  </main>
</body>
</html>
```